Website Design for a Graphic Design Studio in California

We are working with a graphic design company in California.
PLEASE NOTE: We report and ban any designer that reaches out directly to our customers.

Some sites to use for content/competitors and inspiration:

http://quelvint.co.uk
https://www.fendro.studio
https://www.zuplo.io (Client's Favorite)
https://www.merigoldcrafts.com
https://craftwimble.com
https://www.dravinsultonmask.com/us/home/

Thank you for taking the time to consider designing a website for us. We are web developers based in Stockton, CA, USA. Most of our projects go through the same process. Understanding this process may help you win a project with us. We custom-code all of our websites in-house. We don’t have any requirements as to what tools you use for your design, but we prefer Figma files. For any design that we label as four-stars, we send it to the client for review. The client picks the final design they want us to use. Once we complete this process, we will continue to show additional clients all the four-star sites and purchase them later. Your designs will have multiple chances to sell. For better chances of success, we ask that you follow these guidelines.

IMAGES:
If you use any images or icons in the design, we ask that you have a link to the asset so we can purchase the image/icon. Most of the designs we submit do not have the customer’s images on them unless they have some great images. Be creative; show us the feeling you are trying to portray with your image choices. Use any royalty-free site you choose. We subscribe to Tessaly and mainly use their images, but we can purchase images outside of Tessaly. PLEASE NOTE: we will not submit designs to clients with watermarks on the images.

FONTS:
We ask that you identify the fonts used in the design. This can be done in a message if you want. We typically use Brindle Fonts and Tessaly Fonts.

CONTENT:
We're always open to different content and ideas. We often submit designs with stock images so the client can see our vision. We typically take pictures after the website launch to use their images with our vision. Lorem Ipsum is fine for paragraphs, but we ask that you write the headers in correct English. We want to be able to show the vision and identify the sections of the website.

INSPIRATION:
We typically add a couple of links in the brief of websites we like to help you get started in your design.

REVISIONS:
We do not often ask for revisions of the designs unless we see something in the design that may not appeal to the client. If there are slight changes that we want to make, we do that in the development process.

FEEDBACK:
We rarely give feedback on designs during the design process. We are working on many website projects and do not have the time to provide feedback. We usually respond if your request is well thought out and asks specific questions, but a note asking “feedback, please” usually goes unanswered.

```html
<!DOCTYPE html>
<html lang="en">
<head>
<meta charset="utf-8">
<title>Veltora Creative — Graphic Design Studio</title>
<link rel="stylesheet" href="https://fonts.googleapis.com/css2?family=Montserrat:wght@500;600;700;800&family=Jost:wght@300;400;500&display=swap">
<style>
:root{
  --ink:#0a0a0a;
  --black:#000;
  --white:#fff;
  --card:#f4f4f4;
  --muted:#555;
  --star:#b9c41d;
  --photo-dark:#2b2b2b;
  --photo-light:#d9d9d6;
}
*{box-sizing:border-box;margin:0;padding:0}
html,body{width:1200px;height:5303px;overflow:hidden}
body{position:relative;background:var(--white);color:var(--ink);font-family:"Jost",sans-serif}
.abs{position:absolute}
.heading{font-family:"Montserrat",sans-serif;font-weight:800;letter-spacing:.5px;line-height:1}
.photo{position:absolute}

/* header */
.site-header{left:0;top:0;width:1200px;height:90px}
.brand{display:flex;align-items:center;gap:10px;font-family:"Jost",sans-serif;font-weight:400;letter-spacing:3px}
.brand-dot{width:38px;height:38px;border-radius:50%;border:3px solid currentColor}
.site-header .brand{position:absolute;left:31px;top:24px;font-size:24px;color:var(--ink)}
.nav{position:absolute;top:36px;font-family:"Montserrat",sans-serif;font-weight:500;font-size:17px}
.btn-solid{position:absolute;left:998px;top:27px;width:169px;height:41px;background:var(--black);color:var(--white);font-family:"Montserrat",sans-serif;font-size:17px;font-weight:500;display:flex;align-items:center;justify-content:center}

/* hero */
.hero-band{left:0;top:90px;width:1200px;height:684px;background:linear-gradient(120deg,#1a1a1a,#050505 60%)}
.hero-photo{left:47px;top:200px;width:531px;height:708px;background:linear-gradient(160deg,#3a3c40 0%,#9a9ca0 45%,#eeeeec 75%,#f7f7f5 100%)}
.hero-title{left:667px;top:204px;color:var(--white);font-size:68px;line-height:84px}
.hero-sub{left:667px;top:458px;color:var(--white);font-size:35px;font-weight:400}
.btn-outline{position:absolute;border:3px solid var(--white);color:var(--white);font-family:"Montserrat",sans-serif;font-weight:500;font-size:18px;display:flex;align-items:center;justify-content:center}

/* services */
.services-title{left:68px;top:1005px;font-size:70px;line-height:84px}
.btn-view{left:76px;top:1292px;width:163px;height:40px;background:var(--black);color:var(--white);font-family:"Montserrat",sans-serif;font-weight:600;font-size:17px;display:flex;align-items:center;justify-content:center}
.service-card{position:absolute;width:321px;height:288px;background:var(--card);padding:30px 32px}
.service-card svg{width:92px;height:92px;display:block}
.service-card h3{font-family:"Montserrat",sans-serif;font-weight:600;font-size:30px;margin-top:10px}
.service-card p{font-size:17px;color:var(--muted);line-height:22px;margin-top:22px;width:265px}
.service-card a{display:inline-block;margin-top:14px;font-size:18px;color:var(--ink);text-decoration:underline}

/* about */
.about-photo{left:0;top:1743px;width:603px;height:618px;background:linear-gradient(180deg,#3a3a38 0%,#2a2a2a 65%,#d4d4d2 85%,#bdbdbb 100%)}
.about-panel{left:603px;top:1828px;width:597px;height:533px;background:var(--black)}
.about-title{left:679px;top:1873px;color:var(--white);font-size:70px;line-height:86px}
.about-text{left:679px;top:2050px;width:460px;color:var(--white);font-size:17px;line-height:22px;font-weight:300}

/* projects */
.section-title{left:0;width:1200px;text-align:center;font-size:68px}

/* testimonials */
.testimonials-band{left:0;top:3427px;width:1200px;height:582px;background:var(--black)}
.testimonial{position:absolute;top:3676px;width:241px;height:249px;background:var(--card);border-radius:30px;text-align:center;padding-top:16px}
.avatar{width:60px;height:60px;border-radius:50%;margin:0 auto;background:linear-gradient(135deg,#c9b79a,#3a3430)}
.testimonial h4{font-family:"Montserrat",sans-serif;font-weight:700;font-size:15px;margin-top:6px}
.testimonial p{font-family:"Montserrat",sans-serif;font-size:10.5px;line-height:16px;color:var(--muted);width:180px;margin:10px auto 0}
.stars{color:var(--star);font-size:24px;letter-spacing:4px;margin-top:10px}

/* pricing */
.price-card{position:absolute;top:4238px;width:305px;height:463px;background:var(--card);text-align:center;padding-top:52px;font-family:"Montserrat",sans-serif}
.price-card.featured{background:var(--black);color:var(--white)}
.price-card h4{font-size:22px;font-weight:600}
.price-card .amount{font-size:52px;font-weight:700;margin-top:12px;line-height:1}
.price-card .period{font-size:13px;font-weight:600;margin-top:6px}
.price-card ul{list-style:none;margin-top:32px;font-size:14.5px;font-weight:500}
.price-card li{height:35px}
.choose{display:inline-flex;align-items:center;gap:6px;margin-top:20px;height:45px;padding:0 14px;border:2px solid currentColor;border-radius:14px;font-size:15px;font-weight:600}

/* footer */
.site-footer{left:0;top:4826px;width:1200px;height:477px;background:var(--black);color:var(--white)}
.footer-brand{position:absolute;left:0;top:108px;width:1200px;justify-content:center;font-size:34px;color:var(--white)}
.footer-brand .brand-dot{width:56px;height:56px}
.footer-nav{position:absolute;top:222px;left:0;width:1200px;display:flex;justify-content:center;font-family:"Montserrat",sans-serif;font-size:27px;font-weight:500}
.footer-nav span{padding:0 34px;border-right:3px solid var(--white);height:70px;line-height:70px}
.footer-nav span:last-child{border-right:none}
.contact{position:absolute;top:332px;left:0;width:1200px;display:flex;justify-content:center;gap:80px;font-size:24px}
.contact div{display:flex;align-items:center;gap:14px}
.copyright{position:absolute;top:416px;width:1200px;text-align:center;font-size:13px}
</style>
</head>
<body>

<header class="site-header abs">
  <div class="brand"><span class="brand-dot"></span>VELTORA</div>
  <span class="nav" style="left:311px">HOME</span>
  <span class="nav" style="left:434px">ABOUT</span>
  <span class="nav" style="left:578px">SERVICES</span>
  <span class="nav" style="left:731px">PROJECTS</span>
  <span class="nav" style="left:891px">BLOG</span>
  <span class="btn-solid">GET A QUOTE</span>
</header>

<section class="hero">
  <div class="hero-band abs"></div>
  <div class="photo hero-photo" role="img" aria-label="Designer's desk with a monitor showing layout work, markers and glasses"></div>
  <h1 class="hero-title heading abs">BUILDING<br>YOUR<br>BRAND</h1>
  <p class="hero-sub abs">One Step at a Time</p>
  <span class="btn-outline" style="left:663px;top:541px;width:171px;height:44px">GET A QUOTE</span>
</section>

<section class="services">
  <h2 class="services-title heading abs">WHAT<br>WE<br>DO</h2>
  <span class="btn-view abs">VIEW ALL</span>

  <article class="service-card" style="left:393px;top:1002px">
    <svg viewBox="0 0 92 92" fill="none" stroke="#111" stroke-width="3"><rect x="6" y="6" width="80" height="80"/><path d="M46 18 L66 52 L46 76 L26 52 Z"/><circle cx="46" cy="52" r="6"/></svg>
    <h3>Logo Design</h3>
    <p>We care success relationships fuel success we love building</p>
    <a>READ MORE</a>
  </article>
  <article class="service-card" style="left:761px;top:1002px">
    <svg viewBox="0 0 92 92" fill="none" stroke="#111" stroke-width="3"><path d="M10 40 L46 22 L82 40 L82 84 L10 84 Z"/><path d="M10 40 L82 40"/><path d="M46 22 L46 84"/><path d="M38 12 L46 2 L54 12"/></svg>
    <h3>Packaging</h3>
    <p>We care success relationships fuel success we love building</p>
    <a>READ MORE</a>
  </article>
  <article class="service-card" style="left:393px;top:1344px">
    <svg viewBox="0 0 92 92" fill="none" stroke="#111" stroke-width="3"><rect x="4" y="14" width="84" height="62"/><path d="M4 26 H88"/><rect x="14" y="36" width="64" height="28" stroke-dasharray="5 4"/></svg>
    <h3>Branding</h3>
    <p>We care success relationships fuel success we love building</p>
    <a>READ MORE</a>
  </article>
  <article class="service-card" style="left:761px;top:1344px">
    <svg viewBox="0 0 92 92" fill="none" stroke="#111" stroke-width="3"><rect x="8" y="18" width="70" height="54"/><path d="M30 72 L26 86 M56 72 L60 86"/><path d="M30 60 L72 10 L80 18 L40 64 Z"/></svg>
    <h3>illustration</h3>
    <p>We care success relationships fuel success we love building</p>
    <a>READ MORE</a>
  </article>
</section>

<section class="about">
  <div class="photo about-photo" role="img" aria-label="Studio reception area with dark feature wall, waiting chairs and a plant"></div>
  <div class="about-panel abs"></div>
  <h2 class="about-title heading abs">ABOUT<br>US</h2>
  <p class="about-text abs">As a full-service branding and package design agency. We are experts at increasing the value of your brand with imagination, ingenuity and passion.<br>We know that for your business to thrive, all aspects of your branding &amp; marketing need to work together. That's why our proven process builds from the research phase to final asset delivery.</p>
  <span class="btn-outline" style="left:675px;top:2264px;width:171px;height:43px">READ MORE</span>
</section>

<section class="projects">
  <h2 class="section-title heading abs" style="top:2507px">CLIENT PROJECTS</h2>
  <div class="photo" style="left:99px;top:2663px;width:479px;height:299px;background:linear-gradient(90deg,#d9cfb8,#c9a26f 55%,#9a6c3f)" role="img" aria-label="Office reception desk with a receptionist and birch-tree wall mural"></div>
  <div class="photo" style="left:626px;top:2663px;width:479px;height:299px;background:linear-gradient(180deg,#eeeeee,#d2d2d2 70%,#3a3a3a)" role="img" aria-label="Bright waiting room with client branding on the wall"></div>
  <div class="photo" style="left:97px;top:3044px;width:294px;height:272px;background:linear-gradient(160deg,#3a3c40,#a8a9ab 50%,#f2f2f0)" role="img" aria-label="Monitor showing design layout work on a studio desk"></div>
  <div class="abs" style="left:457px;top:3044px;width:294px;height:272px;display:flex;align-items:center;justify-content:center;gap:12px">
    <span style="width:28px;height:28px;background:#1d6fa5"></span>
    <span style="font-family:'Montserrat',sans-serif;font-weight:700;font-size:30px;color:#1d4f8f">HARBISON</span>
  </div>
  <div class="photo" style="left:811px;top:3044px;width:296px;height:272px;background:linear-gradient(180deg,#3a3a38,#262626 70%,#8a8a88)" role="img" aria-label="Studio wall sign mockup in a waiting room"></div>
</section>

<section class="testimonials">
  <div class="testimonials-band abs"></div>
  <h2 class="section-title heading abs" style="top:3512px;color:var(--white)">TESTIMONIALS</h2>
  <div class="testimonial" style="left:183px">
    <div class="avatar" role="img" aria-label="Client portrait"></div>
    <h4>John Doe</h4>
    <p>Lorem ipsum dolor sit amet, consectetur adipiscing elit, sed do eiusmod tempor incididunt ut labore et dolore magna aliqua.</p>
    <div class="stars">★★★★★</div>
  </div>
  <div class="testimonial" style="left:486px">
    <div class="avatar" role="img" aria-label="Client portrait"></div>
    <h4>John Doe</h4>
    <p>Lorem ipsum dolor sit amet, consectetur adipiscing elit, sed do eiusmod tempor incididunt ut labore et dolore magna aliqua.</p>
    <div class="stars">★★★★★</div>
  </div>
  <div class="testimonial" style="left:788px">
    <div class="avatar" role="img" aria-label="Client portrait"></div>
    <h4>John Doe</h4>
    <p>Lorem ipsum dolor sit amet, consectetur adipiscing elit, sed do eiusmod tempor incididunt ut labore et dolore magna aliqua.</p>
    <div class="stars">★★★★★</div>
  </div>
</section>

<section class="pricing">
  <h2 class="section-title heading abs" style="top:4084px">PRICING</h2>
  <div class="price-card" style="left:82px">
    <h4>Premium Pack</h4><div class="amount">$99</div><div class="period">PER MONTH</div>
    <ul><li>Off-Peak Hours</li><li>Standard Fitness Classes</li><li>Personalized Workout Program</li><li>Personal Training Session</li><li>Family Fitness Session</li></ul>
    <span class="choose">Choose Plan <svg width="14" height="12" viewBox="0 0 14 12"><path d="M0 6H10M7 2L11 6L7 10" stroke="currentColor" stroke-width="2.5" fill="none"/></svg></span>
  </div>
  <div class="price-card featured" style="left:447px">
    <h4>BASIC PACK</h4><div class="amount">$15</div><div class="period" style="font-weight:500">PER DAY</div>
    <ul><li>Off-Peak Hours</li><li>Standard Fitness Classes</li><li>Personalized Workout Program</li><li>Personal Training Session</li><li>Family Fitness Session</li></ul>
    <span class="choose">Choose Plan <svg width="14" height="12" viewBox="0 0 14 12"><path d="M0 6H10M7 2L11 6L7 10" stroke="currentColor" stroke-width="2.5" fill="none"/></svg></span>
  </div>
  <div class="price-card" style="left:813px">
    <h4>Premium Pack</h4><div class="amount">$99</div><div class="period">PER MONTH</div>
    <ul><li>Off-Peak Hours</li><li>Standard Fitness Classes</li><li>Personalized Workout Program</li><li>Personal Training Session</li><li>Family Fitness Session</li></ul>
    <span class="choose">Choose Plan <svg width="14" height="12" viewBox="0 0 14 12"><path d="M0 6H10M7 2L11 6L7 10" stroke="currentColor" stroke-width="2.5" fill="none"/></svg></span>
  </div>
</section>

<footer class="site-footer abs">
  <div class="brand footer-brand"><span class="brand-dot"></span>VELTORA CREATIVE</div>
  <nav class="footer-nav"><span>HOME</span><span>ABOUT US</span><span>SERVICES</span><span>PRICES</span><span>FAQS</span></nav>
  <div class="contact">
    <div><svg width="22" height="22" viewBox="0 0 24 24"><path fill="#fff" d="M6.6 10.8a15 15 0 0 0 6.6 6.6l2.2-2.2c.3-.3.7-.4 1-.2 1.1.4 2.3.6 3.6.6.6 0 1 .4 1 1V20c0 .6-.4 1-1 1A17 17 0 0 1 3 4c0-.6.4-1 1-1h3.5c.6 0 1 .4 1 1 0 1.3.2 2.5.6 3.6.1.3 0 .7-.2 1z"/></svg>888 888 8888</div>
    <div><svg width="26" height="20" viewBox="0 0 26 20"><rect width="26" height="20" fill="#fff"/><path d="M1 1L13 11L25 1" stroke="#000" stroke-width="2" fill="none"/></svg>info@veltoracreative.com</div>
  </div>
  <p class="copyright">Copyright 2024 Lumenfield Group. All Rights Reserved.</p>
</footer>

</body>
</html>
```